I need creative and unique business card design using my company logo. Ok to change logo color. We are a small brokerage doing both Real Estate and Mortgage services. Need to have the follow on business card;
1. agent name - Mila Fenton - Realtor
2. cell - 949-555-0182
3. license number - DRE 04917362
4. business name - Brightway Estates & Lending, Inc
5. business office - 626-555-0147
6. business address - 287 W. Larkmoor Ave #214, Arcadia CA 91088
7. business logo - attached (ok to use different color on logo)

```html
<!DOCTYPE html>
<html lang="en">
<head>
<meta charset="utf-8">
<title>Brightway Estates &amp; Lending – Business Card</title>
<link rel="stylesheet" href="https://fonts.googleapis.com/css2?family=Montserrat:wght@400;500;800&display=swap">
<style>
  :root {
    --stage: #3a3a3a;
    --brand-blue: #2f67ad;
    --brand-deep: #24397a;
    --brand-light: #4a9fda;
    --ink: #3b3b3b;
    --paper: #ffffff;
  }
  * { margin: 0; padding: 0; box-sizing: border-box; }
  html, body { width: 1200px; height: 689px; overflow: hidden; }
  body {
    background: var(--stage);
    font-family: "Montserrat", sans-serif;
    position: relative;
  }
  .card {
    position: absolute;
    width: 540px;
    height: 309px;
    overflow: hidden;
    box-shadow: 0 14px 30px rgba(0,0,0,.45);
  }

  /* Front side */
  .card--front {
    left: 40px; top: 60px;
    background: var(--brand-blue);
  }
  .front-panel {
    position: absolute; inset: 0;
    background: linear-gradient(120deg, var(--brand-deep) 0%, #3b5596 45%, #7aa3d2 100%);
    clip-path: polygon(0 0, 52% 0, 100% 100%, 0 100%);
    opacity: .85;
  }
  .front-brand {
    position: absolute; right: 34px; bottom: 40px;
    color: var(--paper);
    font-weight: 500; font-size: 15px;
    letter-spacing: .22em; text-transform: uppercase;
    line-height: 1.6; text-align: right;
  }

  /* Back side */
  .card--back {
    left: 620px; top: 320px;
    background: var(--paper);
  }
  .brand-block {
    position: absolute; left: 36px; top: 72px; width: 230px;
    text-align: center;
  }
  .brand-mark {
    width: 62px; height: 62px; margin: 0 auto 22px;
    background: linear-gradient(135deg, var(--brand-deep), var(--brand-light));
  }
  .brand-name {
    color: var(--brand-blue);
    font-weight: 500; font-size: 15px;
    letter-spacing: .2em; text-transform: uppercase; line-height: 1.6;
  }
  .divider {
    position: absolute; left: 290px; top: 56px;
    width: 1px; height: 170px; background: var(--brand-blue);
  }
  .contact {
    position: absolute; left: 312px; top: 58px;
    color: var(--ink); font-size: 12.5px; line-height: 1.45;
  }
  .agent-name {
    color: var(--brand-blue); font-weight: 800; font-size: 19px;
    letter-spacing: .02em; text-transform: uppercase;
  }
  .agent-title { margin-bottom: 10px; }
  .contact-row { display: flex; align-items: center; gap: 7px; }
  .contact-row svg { width: 12px; height: 12px; flex: none; }
  .address { margin: 14px 0 4px; }
  .license {
    position: absolute; left: 312px; bottom: 40px;
    color: var(--brand-blue); font-weight: 500; font-size: 14px;
  }
</style>
</head>
<body>
  <section class="card card--front">
    <div class="front-panel"></div>
    <p class="front-brand">Brightway<br>Estates &amp; Lending, Inc</p>
  </section>

  <section class="card card--back">
    <div class="brand-block">
      <div class="brand-mark"></div>
      <p class="brand-name">Brightway<br>Estates &amp; Lending, Inc</p>
    </div>
    <div class="divider"></div>
    <div class="contact">
      <p class="agent-name">Mila Fenton</p>
      <p class="agent-title">Realtor</p>
      <p class="contact-row">
        <svg viewBox="0 0 12 12" aria-hidden="true"><rect x="3" y="0.8" width="6" height="10.4" rx="1.2" fill="none" stroke="#2f67ad" stroke-width="1.2"/></svg>
        949-555-0182
      </p>
      <p class="address">287 W. Larkmoor Ave #214,<br>Arcadia CA 91088</p>
      <p class="contact-row">
        <svg viewBox="0 0 12 12" aria-hidden="true"><path d="M3 1.5 L5 3.8 L4 5 Q5 7.2 7 8 L8.2 7 L10.5 9 L9 10.8 Q4.5 10.5 1.2 3 Z" fill="#2f67ad"/></svg>
        626-555-0147
      </p>
    </div>
    <p class="license">DRE 04917362</p>
  </section>
</body>
</html>
```